Grill, Tunes & Summer Feast.

I need an A3 Poster, Insta Square and Facebook Event Cover photo for a Grill Tunes and Feast Event. Details as follows:

Name: Grill, Tunes and Summer Feast
12pm - Late. Jan 26th at Tallow Creek Taphousing
Acts:
Tin Sparrow - 7pm
Copper Wire & Slow Morris - 3pm - 7pm
Derek Holloway - 12pm -3pm

Free BBQ 2-4pm.

```html
<!DOCTYPE html>
<html lang="en">
<head>
<meta charset="utf-8">
<title>Grill, Tunes &amp; Summer Feast – Event Cover</title>
<link href="https://fonts.googleapis.com/css2?family=Bitter:wght@300;700;900&family=Bree+Serif&display=swap" rel="stylesheet">
<style>
  :root {
    --page: #f1f1f0;
    --slate: #2a3333;
    --slate-line: #46504f;
    --charcoal: #1b2024;
    --ember: #df3d24;
    --cream: #ede3d8;
    --ink: #1b2024;
    --foam: #f4efe4;
    --amber: #e9a91c;
    --amber-deep: #b7670f;
    --wood: #a8581f;
    --wood-deep: #6e3412;
    --plate: #efe6da;
  }
  * { margin: 0; padding: 0; box-sizing: border-box; }
  html, body { width: 1200px; height: 800px; overflow: hidden; background: var(--page); }

  .cover {
    position: absolute; left: 20px; top: 96px;
    width: 1160px; height: 607px;
    background: var(--slate);
    overflow: hidden;
    font-family: "Bitter", Georgia, serif;
  }
  .cover__panel { position: absolute; left: 0; top: 0; }

  /* artwork areas */
  .art { position: absolute; }
  .art--guitar {
    left: 30px; top: 62px; width: 70px; height: 478px;
    border-radius: 30px 30px 60px 60px;
    background: linear-gradient(180deg, #262d2f 0%, #2c3434 60%, #313a39 100%);
  }
  .art--mugs {
    left: 122px; top: 150px; width: 402px; height: 268px;
    border-radius: 46px 46px 24px 24px;
    background: linear-gradient(180deg, var(--foam) 0%, #efd9a0 16%, var(--amber) 34%, #f2b92a 62%, var(--amber-deep) 100%);
  }
  .art--platter {
    left: 118px; top: 404px; width: 408px; height: 168px;
    border-radius: 50%;
    background: radial-gradient(ellipse at 50% 40%, #c4412a 0%, var(--wood) 45%, var(--wood-deep) 80%, var(--plate) 100%);
  }

  .brand-tab { position: absolute; left: 161px; top: 0; width: 321px; height: 160px; }
  .brand-tab__shape { position: absolute; left: 0; top: 0; }
  .brand-tab__name {
    position: absolute; left: 0; top: 44px; width: 321px;
    text-align: center; color: var(--cream);
    font-family: "Bree Serif", Georgia, serif;
    font-size: 30px; line-height: 34px; letter-spacing: 1px;
  }

  .headline {
    position: absolute; left: 560px; top: 48px; width: 544px;
    text-align: center; color: var(--ember); text-transform: uppercase;
    font-weight: 900; white-space: nowrap;
  }
  .headline__line { display: block; font-size: 64px; line-height: 72px; letter-spacing: -0.5px; }
  .headline__amp { display: block; font-size: 32px; line-height: 32px; margin: -4px 0 -2px; }

  .date__month {
    position: absolute; left: 558px; top: 302px; width: 70px; text-align: center;
    color: var(--ember); font-weight: 300; font-size: 32px; line-height: 32px; letter-spacing: 1px;
    transform: rotate(-90deg);
  }
  .date__day {
    position: absolute; left: 608px; top: 262px;
    color: var(--cream); font-weight: 700; font-size: 100px; line-height: 110px; letter-spacing: -2px;
  }
  .date__rule { position: absolute; left: 734px; top: 280px; width: 1px; height: 74px; background: var(--cream); }
  .venue {
    position: absolute; left: 752px; top: 274px; color: var(--cream);
    font-weight: 300; font-size: 27px; line-height: 38px;
    text-transform: uppercase; white-space: nowrap;
  }

  .lineup { position: absolute; left: 576px; top: 373px; width: 508px; list-style: none; }
  .lineup__act {
    height: 36px; margin-bottom: 10px; background: var(--cream);
    color: var(--ink); text-align: center;
    font-weight: 700; font-size: 20px; line-height: 36px;
    text-transform: uppercase; white-space: nowrap;
  }
  .free-bbq {
    position: absolute; left: 576px; top: 510px; width: 508px; text-align: center;
    color: var(--ember); font-weight: 700; font-size: 34px; line-height: 40px;
    letter-spacing: 1.5px; text-transform: uppercase;
  }
</style>
</head>
<body>
  <main class="cover">
    <svg class="cover__panel" width="1160" height="607" viewBox="0 0 1160 607" aria-hidden="true">
      <path d="M32 40 L150 28 L500 30 L620 38 L900 32 L1120 30 L1125 150 L1130 400 L1135 570 L900 574 L600 578 L300 574 L44 582 L38 400 L30 200 Z" fill="var(--charcoal)"/>
    </svg>

    <div class="art art--guitar" role="img" aria-label="Line drawing of an acoustic guitar with music notes"></div>
    <div class="art art--mugs" role="img" aria-label="Photo of two frothy beer mugs clinking together"></div>
    <div class="art art--platter" role="img" aria-label="Photo of a wooden platter of grilled sausages with salad"></div>

    <div class="brand-tab">
      <svg class="brand-tab__shape" width="321" height="160" viewBox="0 0 321 160" aria-hidden="true">
        <path d="M0.5 0 V100 Q0.5 138 60 150 Q160 170 261 150 Q320.5 138 320.5 100 V0" fill="var(--slate)" stroke="var(--slate-line)" stroke-width="1"/>
      </svg>
      <div class="brand-tab__name">TALLOW CREEK<br>TAPHOUSE</div>
    </div>

    <h1 class="headline">
      <span class="headline__line">Grill, Tunes</span>
      <span class="headline__amp">&amp;</span>
      <span class="headline__line">Summer Feast</span>
    </h1>

    <span class="date__month">JAN</span>
    <span class="date__day">26</span>
    <div class="date__rule"></div>
    <p class="venue">12PM at Tallow Creek<br>Taphousing</p>

    <ul class="lineup">
      <li class="lineup__act">Tin Sparrow : 7PM</li>
      <li class="lineup__act">Copper Wire &amp; Slow Morris : 3-7PM</li>
      <li class="lineup__act">Derek Holloway : 12-3PM</li>
    </ul>

    <p class="free-bbq">Free BBQ 2-4PM</p>
  </main>
</body>
</html>
```